Need a Revamped Website - WaveCrestHub.com

I am looking for a website designed for www.wavecresthub.com
The present website has content relating to the Kafue Airwave Forum - an annual meeting for radio practitioners in Zambia. My intention is to change the focus: to make the website a resource hub for radio practitioners in Africa. The site is to have the following:
Featured articles (opinion pieces) contributed by industry insiders.
Links to various radio stations websites
An events calendar focusing on radio related events
News (radio industry updates) etc
The site should also be able to incorporate social media mechanisms such as 'Likes' through to Chatterbook or articles to be shared on Pipline etc.
The focus of the word Summit, for the purposes of the website, should shift. Instead of the meaning "meeting/ convention", it'll shift to connote "height, pinnacle (of radio excellence)".
The design should have a modern, contemporary feel.
Target Market(s)
The main target audience is radio deejays, radio station management, marketers/ advertisers, journalists.

```html
<!DOCTYPE html>
<html lang="en">
<head>
<meta charset="utf-8">
<title>WaveCrest Hub – A Resource Hub for Radio Practitioners in Africa</title>
<link rel="stylesheet" href="https://fonts.googleapis.com/css2?family=Jost:wght@300;400;600;700&family=Open+Sans:wght@400;600;700&family=Arimo:wght@400;700&display=swap">
<style>
:root{
  --blue:#2b8bbd;
  --blue-light:#3aa0cf;
  --blue-dark:#1f6f9c;
  --blue-deep:#1b6592;
  --ink:#1c1c1c;
  --text:#333;
  --muted:#555;
  --link:#1a6fa3;
  --panel-border:#c9cdd1;
  --panel-head-top:#e4e7ea;
  --panel-head-bottom:#c8ccd0;
  --news-head-top:#7b848b;
  --news-head-bottom:#59626a;
  --meta-bg:#efefef;
  --white:#fff;
}
*{margin:0;padding:0;box-sizing:border-box}
html,body{width:1004px;height:1200px;overflow:hidden}
body{position:relative;background:linear-gradient(#f6f6f6,#eeeeee);font-family:"Open Sans",Arial,sans-serif;color:var(--text);font-size:10px;letter-spacing:-.1px}
a{color:inherit;text-decoration:none}

/* navigation bars */
.main-nav{position:absolute;left:0;width:1004px;background:linear-gradient(var(--blue-light),var(--blue));display:flex;justify-content:center;align-items:center;font-family:"Arimo",Arial,sans-serif;font-weight:700;color:var(--white);text-transform:uppercase;letter-spacing:.3px}
.main-nav.top{top:0;height:50px;font-size:14px;border-top:7px solid var(--blue-dark);border-bottom:1px solid #5fb3d9}
.main-nav.bottom{top:1113px;height:45px;font-size:14px;border-top:1px solid #5fb3d9}
.main-nav .star{margin:0 24px;font-size:13px;position:relative;top:-1px}

/* header */
.site-header{position:absolute;top:50px;left:0;width:1004px;height:102px;background:radial-gradient(ellipse at 30% 50%,#3d9ccb,var(--blue-dark) 80%)}
.logo{position:absolute;left:35px;top:40px;font-family:"Open Sans",Arial,sans-serif;font-weight:700;font-size:38px;color:#eef4f8;letter-spacing:-.5px;line-height:1}
.tagline{position:absolute;left:379px;top:50px;color:#e7f2f8;font-size:12.5px;line-height:15px;letter-spacing:.2px;text-transform:uppercase}
.search{position:absolute;left:779px;top:51px;width:181px;height:26px;background:var(--white);border-radius:13px;box-shadow:inset 0 1px 3px rgba(0,0,0,.3)}
.search svg{position:absolute;right:8px;top:5px}
.search::before{content:"";position:absolute;right:30px;top:3px;width:1px;height:20px;background:#ccc}

/* hero */
.hero{position:absolute;top:152px;left:0;width:1004px;height:291px;background:linear-gradient(90deg,#e6e6e6,#f8f8f8 50%,#ececec);border-bottom:1px solid #ddd}
.hero-photo{position:absolute;left:60px;top:30px;width:485px;height:261px;background:radial-gradient(ellipse at 50% 45%,#d7d0c6 0%,#bdb3a6 45%,rgba(220,220,220,0) 75%)}
.hero-copy{position:absolute;left:566px;top:88px;color:var(--ink);font-family:"Jost",Arial,sans-serif;text-transform:uppercase;letter-spacing:0}
.hero-copy .welcome{font-weight:700;font-size:20.5px;line-height:22px;letter-spacing:.2px}
.hero-copy .line{font-size:37px;line-height:36px;letter-spacing:-.3px}
.hero-copy .light{font-weight:300}
.hero-copy .regular{font-weight:400}
.hero-dots{position:absolute;left:829px;top:261px;display:flex;gap:11px}
.hero-dots span{width:13px;height:13px;border-radius:50%;background:#c5cfd6;box-shadow:inset 0 1px 2px rgba(0,0,0,.25)}
.hero-dots span.active{background:radial-gradient(circle,var(--blue-deep) 35%,#c5cfd6 45%)}

/* breadcrumb */
.breadcrumb{position:absolute;left:30px;top:455px;display:flex;align-items:center;gap:8px;font-size:11px;color:#333}

/* panels */
.panel{position:absolute;background:var(--white);border:1px solid var(--panel-border);box-shadow:0 1px 2px rgba(0,0,0,.08);overflow:hidden}
.panel-head{height:37px;background:linear-gradient(var(--panel-head-top),var(--panel-head-bottom));border-bottom:1px solid #b9bec3;display:flex;align-items:center;padding:0 14px;font-family:"Arimo",Arial,sans-serif;font-size:15px;font-weight:400;color:#2b2b2b;text-transform:uppercase;letter-spacing:0}
.panel-head b{font-weight:700;margin-left:5px}
.panel-head .pill{margin-left:auto;font-size:10.5px;font-weight:400;text-transform:none;padding:3px 6px;background:linear-gradient(#a9afb5,#8f969c);color:var(--white);border:1px solid #858c92}
.read-more{color:var(--link);margin-left:6px}

.about{left:28px;top:479px;width:652px;height:162px}
.about-body{padding:11px 12px;line-height:14px;position:relative;height:123px;background:linear-gradient(90deg,#fff 60%,#f1f3f5)}
.about-body p{position:relative}
.about-body p.narrow{width:430px}
.about-art{position:absolute;right:0;bottom:0;width:190px;height:60px;background:linear-gradient(180deg,rgba(255,255,255,0),#dfe3e6)}

.articles{left:28px;top:654px;width:652px;height:440px}
.article-body{padding:12px 12px 0;height:89px;line-height:14px}
.article:first-of-type .article-body{height:83px}
.article-body h3{font-size:10px;font-weight:700;color:var(--ink);line-height:14px}
.article-meta{height:43px;background:var(--meta-bg);display:flex;align-items:center;padding:0 12px;color:#444}
.article-meta .sep{width:1px;height:9px;background:#555;margin:0 12px}
.article-meta u{color:#333}
.like-btn{display:inline-flex;align-items:center;gap:3px;border:1px solid #9fb0c9;background:linear-gradient(#f2f4f8,#dfe4ec);border-radius:2px;padding:3px 5px;color:#3b5998;font-family:Arial,sans-serif;font-size:10.5px;margin-right:6px}
.social-mark{display:inline-block;width:11px;height:11px;background:#3b5998;margin-right:4px;vertical-align:-1px}
.social-mark.cyan{background:#2aa9e0;margin-left:5px;margin-right:0}

.news{left:692px;top:479px;width:279px;height:416px}
.news .panel-head{background:linear-gradient(var(--news-head-top),var(--news-head-bottom));color:var(--white);border-bottom-color:#4d555c}
.news .panel-head .pill{background:#4a5158;border-color:#3d434a}
.news-item{padding:12px 13px 0;border-bottom:1px solid #dcdcdc;line-height:14px;overflow:hidden}
.news-item.first{height:133px}
.news-item.second{height:125px}
.news-item.third{height:119px;border-bottom:none}
.news-item h3{font-size:10.5px;font-weight:700;color:var(--ink);line-height:14px}
.news-item time{display:block;font-size:9px;color:#444;line-height:14px;margin:0 0 14px}
.ext{display:inline-block;width:9px;height:9px;border:1px solid #999;margin-left:4px;vertical-align:0}

.events{left:692px;top:907px;width:279px;height:187px}
.events-title{position:absolute;left:12px;top:12px;font-family:"Arimo",Arial,sans-serif;font-size:14px;font-weight:400;line-height:14px;color:#2b2b2b}
.events-title b{display:block}
.events-icon{position:absolute;left:14px;top:50px;width:54px;height:52px;border:1px solid #aac3da;background:linear-gradient(#5c9ad0 0 9px,#eef4fa 9px)}
.events-brand{position:absolute;left:14px;top:110px;font-weight:700;font-size:11px;line-height:13px;color:#c3c7cb;text-transform:uppercase}
.cal-arrows{position:absolute;left:15px;top:155px;display:flex;gap:2px}
.cal-arrows span{width:18px;height:18px;border:1px solid #c0c0c0;background:linear-gradient(#fff,#e7e7e7);display:flex;align-items:center;justify-content:center}
.calendar{position:absolute;left:97px;top:12px;width:171px;border-collapse:separate;border-spacing:1px;font-family:"Arimo",Arial,sans-serif;font-size:11px;text-align:center;background:#fff;letter-spacing:0}
.calendar caption{background:linear-gradient(#f4f4f4,#dedede);font-weight:700;font-size:13px;color:#333;padding:2px 0;border:1px solid #d0d0d0}
.calendar th{background:#e8e8e8;font-size:10px;color:#444;height:13px}
.calendar td{background:#dcdcdc;height:19px;color:#222}
.calendar td.out{background:#ebebeb;color:#bdbdbd}
.calendar td.busy{background:#b9b9b9}
.calendar td.today{background:#9a9a9a;color:#222}

/* footer */
.site-footer{position:absolute;top:1158px;left:0;width:1004px;height:42px;background:var(--blue-deep);color:#d8e8f2;font-size:10.5px;letter-spacing:.3px;display:flex;justify-content:center;align-items:center;gap:4px}
</style>
</head>
<body>

<nav class="main-nav top" aria-label="Main">
  <a href="#">Home</a><span class="star">★</span>
  <a href="#">About</a><span class="star">★</span>
  <a href="#">Articles</a><span class="star">★</span>
  <a href="#">Gallery</a><span class="star">★</span>
  <a href="#">Partners</a><span class="star">★</span>
  <a href="#">Events</a><span class="star">★</span>
  <a href="#">Contact</a>
</nav>

<header class="site-header">
  <div class="logo">WAVECREST HUB</div>
  <p class="tagline">Better programming. Free speech.<br>Intelligent communication. Great entertainment</p>
  <div class="search">
    <svg width="16" height="16" viewBox="0 0 16 16" aria-hidden="true"><circle cx="6.5" cy="6.5" r="4.5" fill="none" stroke="#8a8a8a" stroke-width="2"/><line x1="10" y1="10" x2="14" y2="14" stroke="#8a8a8a" stroke-width="2.4" stroke-linecap="round"/></svg>
  </div>
</header>

<section class="hero">
  <div class="hero-photo" role="img" aria-label="Group of five smiling radio professionals in suits, the one in the centre holding a globe"></div>
  <div class="hero-copy">
    <div class="welcome">Welcome to WaveCrest Hub</div>
    <div class="line light">A resource hub for</div>
    <div class="line regular">Radio practitioners</div>
    <div class="line light">in Africa</div>
  </div>
  <div class="hero-dots"><span class="active"></span><span></span><span></span><span></span><span></span></div>
</section>

<div class="breadcrumb">
  <svg width="10" height="10" viewBox="0 0 10 10" aria-hidden="true"><path d="M1 5 5 1.5 9 5M2.5 4v5h5V4" fill="none" stroke="#444" stroke-width="1.2"/></svg>
  <span>WaveCrest Hub</span>
</div>

<section class="panel about">
  <h2 class="panel-head">About <b>WaveCrest Hub</b></h2>
  <div class="about-body">
    <div class="about-art" role="img" aria-label="Row of satellite dishes fading into the background"></div>
    <p>Lorem ipsum dolor sit amet consectetur adipiscing elit. Sed accumsan tempus lobortis. Pellentesque habitant morbi tristique senectus et netus et malesuada fames ac turpis egestas.</p>
    <p class="narrow">Fusce diam libero congue vel volutpat ut faucibus non arcu. Donec mollis sem nec mollis vehicula turpis turpis convallis velit nec volutpat tellus ante sit amet erat. Nunc ipsum lectus commodo in rutrum in suscipit ut lorem. Quisque vitae ipsum pharetra purus eleifend consectetur et id lorem. Praesent mollis magna id risus tristique sed facilisis quam egestas. <a class="read-more" href="#">read more...</a></p>
  </div>
</section>

<section class="panel articles">
  <h2 class="panel-head">Featured <b>Articles</b><a class="pill" href="#">Read all</a></h2>

  <article class="article">
    <div class="article-body">
      <h3>Lorem ipsum dolor sit amet consectetur adipiscing elit.</h3>
      <p>Sed accumsan tempus lobortis. Pellentesque habitant morbi tristique senectus et netus et malesuada fames ac turpis egestas. Fusce diam libero congue volutpat. Praesent mollis magna id risus tristique sed facilisis quam egestas. Nulla congue, elit eget mattis fermentum, sem enim auctor lacus, quis viverra augue mauris sit amet enim. <a class="read-more" href="#">read more...</a></p>
    </div>
    <div class="article-meta">
      <span>Posted by: <u>Daniel Mwale</u></span><span class="sep"></span>
      <span>March 03, 2011</span><span class="sep"></span>
      <span class="like-btn"><svg width="11" height="11" viewBox="0 0 11 11" aria-hidden="true"><path d="M1 5h2v5H1zM4 5l2-4c1 0 1.5.7 1.2 2L7 4h3l-1 6H4z" fill="#3b5998"/></svg>Like</span>
      <span><i class="social-mark" aria-hidden="true"></i>3 people like this.</span><span class="sep"></span>
      <span>Share this on<i class="social-mark cyan" aria-hidden="true"></i></span>
    </div>
  </article>

  <article class="article">
    <div class="article-body">
      <h3>Lorem ipsum dolor sit amet consectetur adipiscing elit.</h3>
      <p>Sed accumsan tempus lobortis. Pellentesque habitant morbi tristique senectus et netus et malesuada fames ac turpis egestas. Fusce diam libero congue volutpat. Praesent mollis magna id risus tristique sed facilisis quam egestas. Nulla congue, elit eget mattis fermentum, sem enim auctor lacus, quis viverra augue mauris sit amet enim. <a class="read-more" href="#">read more...</a></p>
    </div>
    <div class="article-meta">
      <span>Posted by: <u>Daniel Mwale</u></span><span class="sep"></span>
      <span>March 03, 2011</span><span class="sep"></span>
      <span class="like-btn"><svg width="11" height="11" viewBox="0 0 11 11" aria-hidden="true"><path d="M1 5h2v5H1zM4 5l2-4c1 0 1.5.7 1.2 2L7 4h3l-1 6H4z" fill="#3b5998"/></svg>Like</span>
      <span><i class="social-mark" aria-hidden="true"></i>3 people like this.</span><span class="sep"></span>
      <span>Share this on<i class="social-mark cyan" aria-hidden="true"></i></span>
    </div>
  </article>

  <article class="article">
    <div class="article-body">
      <h3>Lorem ipsum dolor sit amet consectetur adipiscing elit.</h3>
      <p>Sed accumsan tempus lobortis. Pellentesque habitant morbi tristique senectus et netus et malesuada fames ac turpis egestas. Fusce diam libero congue volutpat. Praesent mollis magna id risus tristique sed facilisis quam egestas. Nulla congue, elit eget mattis fermentum, sem enim auctor lacus, quis viverra augue mauris sit amet enim. <a class="read-more" href="#">read more...</a></p>
    </div>
    <div class="article-meta">
      <span>Posted by: <u>Daniel Mwale</u></span><span class="sep"></span>
      <span>March 03, 2011</span><span class="sep"></span>
      <span class="like-btn"><svg width="11" height="11" viewBox="0 0 11 11" aria-hidden="true"><path d="M1 5h2v5H1zM4 5l2-4c1 0 1.5.7 1.2 2L7 4h3l-1 6H4z" fill="#3b5998"/></svg>Like</span>
      <span><i class="social-mark" aria-hidden="true"></i>3 people like this.</span><span class="sep"></span>
      <span>Share this on<i class="social-mark cyan" aria-hidden="true"></i></span>
    </div>
  </article>
</section>

<aside class="panel news">
  <h2 class="panel-head">Radio <b>News</b><a class="pill" href="#">RSS</a></h2>
  <div class="news-item first">
    <h3>Lorem ipsum dolor sit amet consectetur adipiscing elit.<i class="ext"></i></h3>
    <time>March 24, 2011</time>
    <p>Pellentesque habitant morbi tristique senectus et netus et malesuada fames ac turpis egestas. Fusce diam libero congue vel volutpat ut faucibus non arcu. <a class="read-more" href="#">read more...</a></p>
  </div>
  <div class="news-item second">
    <h3>Donec mollis sem nec mollis vehicula turpis turpis convallis velit nec.<i class="ext"></i></h3>
    <time>March 24, 2011</time>
    <p>Nunc ipsum lectus commodo in rutrum in suscipit ut lorem. Quisque vitae ipsum pharetra purus eleifend consectetur et id lorem. Praesent mollis magna id risus tristique sed facilisis quam. <a class="read-more" href="#">read more...</a></p>
  </div>
  <div class="news-item third">
    <h3>Nulla congue elit eget mattis fermentum, sem enim auctor lacus quis viverra.<i class="ext"></i></h3>
    <time>March 24, 2011</time>
    <p>Proin laoreet rhoncus orci, nec sagittis odio ornare eget. Aenean ligula arcu, dapibus non fermentum ut iaculis sit amet massa. <a class="read-more" href="#">read more...</a></p>
  </div>
</aside>

<aside class="panel events">
  <h2 class="events-title">LATEST<b>EVENTS</b></h2>
  <div class="events-icon" aria-hidden="true"></div>
  <div class="events-brand">WaveCrest<br>Hub</div>
  <div class="cal-arrows">
    <span><svg width="6" height="8" viewBox="0 0 6 8" aria-hidden="true"><path d="M5 0v8L0 4z" fill="#555"/></svg></span>
    <span><svg width="6" height="8" viewBox="0 0 6 8" aria-hidden="true"><path d="M1 0v8l5-4z" fill="#555"/></svg></span>
  </div>
  <table class="calendar">
    <caption>April 2011</caption>
    <tr><th>S</th><th>M</th><th>T</th><th>W</th><th>T</th><th>F</th><th>S</th></tr>
    <tr><td class="out">27</td><td class="out">28</td><td class="out">29</td><td class="out">30</td><td class="out">31</td><td>1</td><td>2</td></tr>
    <tr><td>3</td><td>4</td><td>5</td><td>6</td><td>7</td><td>8</td><td>9</td></tr>
    <tr><td>10</td><td class="busy">11</td><td class="busy">12</td><td class="busy">13</td><td class="busy">14</td><td class="busy">15</td><td class="busy">16</td></tr>
    <tr><td class="today">17</td><td>18</td><td>19</td><td>20</td><td>21</td><td>22</td><td>23</td></tr>
    <tr><td>24</td><td>25</td><td>26</td><td>27</td><td>28</td><td>29</td><td>30</td></tr>
    <tr><td class="out">1</td><td class="out">2</td><td class="out">3</td><td class="out">4</td><td class="out">5</td><td class="out">6</td><td class="out">7</td></tr>
  </table>
</aside>

<nav class="main-nav bottom" aria-label="Footer">
  <a href="#">Home</a><span class="star">★</span>
  <a href="#">About</a><span class="star">★</span>
  <a href="#">Articles</a><span class="star">★</span>
  <a href="#">Gallery</a><span class="star">★</span>
  <a href="#">Partners</a><span class="star">★</span>
  <a href="#">Events</a><span class="star">★</span>
  <a href="#">Contact</a>
</nav>

<footer class="site-footer">
  <span>© WaveCrest Hub 2011.&nbsp; All Rights Reserved.&nbsp;</span>
  <a href="#">Terms of Use.</a>&nbsp;<a href="#">Privacy Policy.</a>
</footer>

</body>
</html>
```